TALMORK

The business want a professional looking business card. We have a scetch we will add but want the extra upgrade, and would like more suggestions for variations of our business cards.

```html
<!DOCTYPE html>
<html lang="en">
<head>
<meta charset="utf-8">
<title>TALMORK – Business Cards</title>
<link href="https://fonts.googleapis.com/css2?family=Playfair+Display:wght@700&family=Montserrat:wght@400;500&display=swap" rel="stylesheet">
<style>
  :root {
    --page-bg: #2a2a2b;
    --card-bg: #111112;
    --card-bg-matte: #141415;
    --gold: #c9a24a;
    --silver: #8c8c8e;
    --text-light: #f2f2f2;
  }
  * { margin: 0; padding: 0; box-sizing: border-box; }
  html, body { width: 1200px; height: 900px; overflow: hidden; }
  body {
    background: var(--page-bg);
    display: flex;
    flex-direction: column;
    align-items: center;
    justify-content: center;
    gap: 56px;
  }
  .card {
    width: 640px;
    height: 366px;
    border-radius: 26px;
    box-shadow: 0 18px 40px rgba(0,0,0,0.45);
    position: relative;
  }
  /* Front: logo-only card */
  .card--front {
    background: var(--card-bg-matte);
    display: flex;
    align-items: center;
    justify-content: center;
    gap: 18px;
  }
  .brand-mark {
    width: 34px;
    height: 34px;
    border-radius: 50%;
  }
  .brand-name {
    font-family: "Playfair Display", Georgia, serif;
    font-weight: 700;
    letter-spacing: 4px;
  }
  .card--front .brand-mark { background: var(--silver); width: 46px; height: 46px; }
  .card--front .brand-name { color: var(--silver); font-size: 66px; }

  /* Back: contact card */
  .card--back {
    background: var(--card-bg);
    display: flex;
    align-items: center;
    padding: 0 48px 0 44px;
  }
  .brand-lockup {
    width: 230px;
    display: flex;
    align-items: center;
    gap: 12px;
  }
  .card--back .brand-mark { background: var(--gold); width: 26px; height: 26px; }
  .card--back .brand-name { color: var(--gold); font-size: 38px; letter-spacing: 2px; }
  .divider {
    width: 1.5px;
    height: 150px;
    background: var(--gold);
    margin: 0 34px 0 10px;
  }
  .contact { flex: 1; }
  .contact__name {
    font-family: "Playfair Display", Georgia, serif;
    font-weight: 700;
    font-size: 29px;
    color: var(--gold);
    line-height: 1.1;
  }
  .contact__role {
    font-family: "Montserrat", Arial, sans-serif;
    font-size: 15px;
    color: var(--text-light);
    margin: 6px 0 18px;
  }
  .contact__list { list-style: none; }
  .contact__item {
    display: flex;
    align-items: center;
    gap: 10px;
    font-family: "Montserrat", Arial, sans-serif;
    font-size: 15px;
    color: var(--text-light);
    margin-bottom: 7px;
  }
  .contact__icon { width: 14px; height: 14px; flex: none; }
  .contact__icon * { fill: var(--gold); }
</style>
</head>
<body>
  <section class="card card--front" aria-label="Business card front">
    <span class="brand-mark"></span>
    <span class="brand-name">TALMORK</span>
  </section>

  <section class="card card--back" aria-label="Business card back">
    <div class="brand-lockup">
      <span class="brand-mark"></span>
      <span class="brand-name">TALMORK</span>
    </div>
    <div class="divider"></div>
    <div class="contact">
      <h1 class="contact__name">Eirik Solvang Haugen</h1>
      <p class="contact__role">CEO &amp; Founder</p>
      <ul class="contact__list">
        <li class="contact__item">
          <svg class="contact__icon" viewBox="0 0 16 16"><path d="M3 1h3l1.5 4-2 1.3a9 9 0 0 0 4.2 4.2L11 8.5l4 1.5v3a2 2 0 0 1-2 2A13 13 0 0 1 1 3a2 2 0 0 1 2-2z"/></svg>
          004791234567
        </li>
        <li class="contact__item">
          <svg class="contact__icon" viewBox="0 0 16 16"><path d="M1 3h14v10H1z M2 4l6 5 6-5" style="fill:none;stroke:#c9a24a;stroke-width:1.6"/></svg>
          talmork.co@mailbox.com
        </li>
        <li class="contact__item">
          <svg class="contact__icon" viewBox="0 0 16 16"><circle cx="8" cy="8" r="6.5" style="fill:none;stroke:#c9a24a;stroke-width:1.5"/><path d="M1.5 8h13M8 1.5c-3 3.5-3 9.5 0 13M8 1.5c3 3.5 3 9.5 0 13" style="fill:none;stroke:#c9a24a;stroke-width:1.2"/></svg>
          www.talmork.co
        </li>
      </ul>
    </div>
  </section>
</body>
</html>
```